Maple Sprout Menu (Vegetarian Restaurant Concept)

Maple Sprout is a new concept fast casual restaurant
renders are attached so you can see the style of restaurant
Maple Sproutt is a vibrant and modern Vegetarian fast casual restaurant concept that mixes fresh food, energy, great décor, and a comfortable, welcoming atmosphere to provide a memorable and all Vegetarian dining experience.
Our Mission is to be top of mind when consumers think Vegetarian food!
Target Market(s)
the menu is vegetarian and appeals to a broad demographic in USA
Colors
Designer to choose colors to be used in the design.
Requirements
Must have
- well colored and well laid out menu - should not be cartoonish
Nice to have
- For Phots please use the shots in this file:
- https://www.filecrate-example.com/sh/qwx7tr2bnm4kdle/BBBdK_pQrLmNZTHO5E_XYZ_Kb?dl=0
- note these are untouched and you are free to change as needed
Should not have
- Should not be cartoonish - nor kives, forks etc in the design

```html
<!DOCTYPE html>
<html lang="en">
<head>
<meta charset="utf-8">
<title>Maple Sproutt — Menu</title>
<link rel="stylesheet" href="https://fonts.googleapis.com/css2?family=Montserrat:wght@300;400;700;900&display=swap">
<style>
  :root {
    --ink: #000000;
    --leaf: #8dc63f;
    --paper: #ffffff;
    --charcoal: #2b2b2b;
    --rule: #cfcfcf;
  }
  * { margin: 0; padding: 0; box-sizing: border-box; }
  html, body { width: 846px; height: 1200px; overflow: hidden; background: var(--ink); }
  .menu {
    position: relative; width: 846px; height: 1200px; overflow: hidden;
    background: var(--ink); color: var(--paper);
    font-family: "Montserrat", sans-serif; font-weight: 300;
  }
  .hero-photo {
    position: absolute; left: 238px; top: 0; width: 608px; height: 440px;
    background:
      radial-gradient(ellipse 42% 48% at 72% 28%, #c93a3f 0%, #8e1d26 45%, rgba(230,230,230,.9) 70%, rgba(0,0,0,0) 88%),
      radial-gradient(ellipse 36% 55% at 20% 32%, rgba(220,220,220,.55) 0%, rgba(60,60,60,.35) 60%, rgba(0,0,0,0) 100%),
      radial-gradient(ellipse 30% 22% at 22% 80%, rgba(70,110,30,.75) 0%, rgba(0,0,0,0) 100%);
  }
  .brand-band {
    position: absolute; left: 67px; top: 0; width: 171px; height: 360px;
    background: linear-gradient(to bottom, var(--leaf) 0%, #6fa032 45%, #1c2a0c 80%, var(--ink) 100%);
  }
  .brand-dot {
    position: absolute; left: 128px; top: 66px; width: 48px; height: 48px;
    border-radius: 50%; background: #f0a25a;
  }
  .brand-name {
    position: absolute; left: 67px; top: 186px; width: 171px; text-align: center;
    font-weight: 700; font-size: 25px; line-height: 28px; color: var(--charcoal);
  }
  .title-banner { position: absolute; left: 0; top: 0; }
  .section-title {
    position: absolute; font-weight: 700; font-size: 19px; line-height: 22px;
    padding-bottom: 4px; border-bottom: 1.5px solid var(--paper); text-transform: uppercase;
  }
  .item { position: absolute; font-size: 14.3px; line-height: 16px; text-transform: uppercase; white-space: nowrap; }
  .desc { position: absolute; font-size: 12px; line-height: 12px; white-space: nowrap; }
  .left { left: 18px; }
  .right { right: 22px; text-align: right; }
  .divider { position: absolute; left: 421px; top: 418px; width: 3px; height: 630px; background: var(--leaf); }
  .footer { position: absolute; left: 0; top: 1048px; width: 846px; height: 113px; background: var(--leaf); }
  .social-dot { position: absolute; left: 25px; width: 28px; height: 28px; border-radius: 50%; background: var(--paper); }
  .sign-off {
    position: absolute; right: 40px; top: 1078px; font-weight: 900; font-size: 46px; line-height: 52px;
    color: var(--paper); letter-spacing: 1px;
  }
</style>
</head>
<body>
<main class="menu">
  <div class="hero-photo" role="img" aria-label="Photo of a strawberry dessert in a white bowl on a checked cloth with scattered fresh herbs"></div>

  <div class="brand-band"></div>
  <div class="brand-dot"></div>
  <div class="brand-name">Maple<br>Sproutt</div>

  <svg class="title-banner" width="846" height="300" viewBox="0 0 846 300">
    <line x1="285" y1="93" x2="795" y2="93" stroke="var(--rule)" stroke-width="3"/>
    <polygon points="285,107 792,107 766,178 803,251 285,251 314,178" fill="#ffffff" fill-opacity="0.5"/>
    <line x1="285" y1="265" x2="803" y2="265" stroke="var(--rule)" stroke-width="3"/>
    <text x="543" y="210" text-anchor="middle" font-family="Montserrat, sans-serif" font-weight="900" font-size="88" fill="#8dc63f" stroke="#3a0f12" stroke-width="1.5" paint-order="stroke">MENU</text>
  </svg>

  <h2 class="section-title left" style="top:444px;">Salads</h2>
  <p class="item left" style="top:488px;">Brussel Sprout Caesar</p>
  <p class="desc left" style="top:504px;">little gem romaine, toasted torn bread, parmiggiano reggiano</p>
  <p class="item left" style="top:526px;">Heirloom Beet Salad</p>
  <p class="desc left" style="top:543px;">shaved chioggia beet, roasted golden beet, red quinoa</p>
  <p class="desc left" style="top:556px;">little gem, arugula, lemon vinaigrette</p>
  <p class="item left" style="top:578px;">Zesty Black Bean &amp; Corn Salad in Lettuce Cups</p>
  <p class="desc left" style="top:595px;">black beans, avocado and roasted corn topped with feta crumbles</p>
  <p class="desc left" style="top:607px;">in butter lettuce</p>
  <p class="item left" style="top:631px;">Green, Red &amp; White</p>
  <p class="desc left" style="top:648px;">spring leaves, cherry tomatoes, avocado</p>
  <p class="desc left" style="top:660px;">roasted almond and goat cheese</p>

  <h2 class="section-title left" style="top:724px;">Toasts</h2>
  <p class="item left" style="top:769px;">Everything Avocado Toast</p>
  <p class="desc left" style="top:784px;">avocado on whole grain toast with our signature spice blend</p>
  <p class="item left" style="top:806px;">Tomato &amp; Beet Bruschetta</p>
  <p class="item left" style="top:830px;">Vegetable Melt on Garlic Toast</p>

  <h2 class="section-title left" style="top:883px;">Soup</h2>
  <p class="item left" style="top:927px;">Black Bean Chowder</p>

  <div class="divider"></div>

  <h2 class="section-title right" style="top:444px;">Burgers / Wraps / Sandwiches</h2>
  <p class="item right" style="top:488px;">Sweet Potato, Black Bean Veggie Burger</p>
  <p class="desc right" style="top:504px;">with cabbage - pepita slaw</p>
  <p class="item right" style="top:526px;">Roasted Vegetable, Arugula and Hummus Wrap</p>
  <p class="item right" style="top:578px;">Garden Burger</p>
  <p class="item right" style="top:631px;">Beans &amp; Greens Quesaddilla</p>
  <p class="desc right" style="top:648px;">greens, Mexican cheese, beans, avocado, salsa</p>
  <p class="item right" style="top:672px;">Vegetable Burrito</p>
  <p class="desc right" style="top:689px; text-align:left;">greens, Mexican cheese, beans, brown rice, roasted chilli corn<br>avocado, ancho chilli salsa, wheat tortilla</p>

  <h2 class="section-title right" style="top:724px;">Bowls</h2>
  <p class="item right" style="top:769px;">Roasted Vegetable &amp; Spinach</p>
  <p class="item right" style="top:806px;">Sugar Snap Pea &amp; Carrot Soba Noodles</p>
  <p class="item right" style="top:830px;">Whole Grain and Vegetable Buddha</p>
  <p class="item right" style="top:858px;">Orange &amp; Pistacio Quinoa</p>

  <h2 class="section-title right" style="top:883px;">Desserts</h2>
  <p class="item right" style="top:927px;">Strawberry Balsamic Ice Cream Sundae</p>
  <p class="item right" style="top:955px;">Exotic Fruit Bowl</p>
  <p class="item right" style="top:984px;">White and Dark Oatmeal Cookie</p>

  <footer class="footer"></footer>
  <div class="social-dot" style="top:1068px;"></div>
  <div class="social-dot" style="top:1112px;"></div>
  <p class="sign-off">ENJOY!</p>
</main>
</body>
</html>
```